Interior Design/ New Construction interior finishes

Interior Design Website

Target Market(s)

Home builders, New Construction, Renovations, Public

Industry/Entity Type

Construction

Coding

Coded - Design and coding required

Number of Pages Required

1 page

Font styles to use
Sans Serif

Colors

Designer to choose colors to be used in the design.

Requirements
Must have
• Section to upload pictures of projects
• Simple and modern design
• Designer 1 details about myself
• Logo
• Upload section for photos for future jobs
Nice to have
• Sections they can click on to see certain rooms in a house
• Decorating, floral arrangements, holiday decorating.
• I have lots of before and after as well. Maybe a section for those.

```html
<!DOCTYPE html>
<html lang="en">
<head>
<meta charset="utf-8">
<title>Norvale Designs — Interior Design</title>
<link href="https://fonts.googleapis.com/css2?family=Josefin+Sans:wght@300;400;600&family=Open+Sans:wght@400;600;700;800&display=swap" rel="stylesheet">
<style>
:root{
  --ink:#222222;
  --muted:#555555;
  --navy:#1f3550;
  --accent:#f7a11a;
  --strip:#eef0f3;
  --footer:#eeeeee;
  --line:#d6d6d6;
  --white:#ffffff;
  --black:#000000;
}
*{margin:0;padding:0;box-sizing:border-box}
html,body{width:1200px;height:2687px;overflow:hidden;background:var(--white)}
body{position:relative;font-family:"Josefin Sans",sans-serif;color:var(--ink)}
.abs{position:absolute}

/* header */
.site-header{position:absolute;left:0;top:0;width:1200px;height:97px;background:var(--white);z-index:3}
.brand{position:absolute;left:143px;top:0;width:170px;height:134px;z-index:4}
.brand-name{position:absolute;left:0;width:170px;top:78px;text-align:center;font-size:24px;letter-spacing:1px;color:var(--ink);font-weight:400}
.brand-dot{position:absolute;left:61px;top:10px;width:48px;height:48px;border:2px solid var(--ink);border-radius:50%}
.contact-item{position:absolute;top:14px;display:flex;align-items:center;gap:16px}
.contact-icon{width:42px;height:38px;border:1px solid #9a9a9a;display:flex;align-items:center;justify-content:center}
.contact-label{font-family:"Open Sans",sans-serif;font-weight:700;font-size:13px;color:var(--navy)}
.contact-value{font-family:"Open Sans",sans-serif;font-size:12px;color:var(--muted);margin-top:3px}
.btn-contact{position:absolute;left:856px;top:14px;width:183px;height:36px;background:var(--accent);color:var(--white);font-family:"Open Sans",sans-serif;font-weight:700;font-size:13px;display:flex;align-items:center;justify-content:center;letter-spacing:.3px}
.main-nav{position:absolute;top:64px;left:349px;width:690px;display:flex;justify-content:space-between;font-size:10px;letter-spacing:2px;color:#444}

/* hero */
.hero{position:absolute;left:0;top:97px;width:1200px;height:598px;background:linear-gradient(180deg,#4a4a48 0%,#5b5750 35%,#3d5866 62%,#4c5e3a 82%,#3b4a2a 100%)}
.hero-shade{position:absolute;inset:0;background:rgba(0,0,0,.25)}
.hero-title{position:absolute;left:0;width:1200px;top:236px;text-align:center;font-family:"Open Sans",sans-serif;font-weight:800;font-size:40px;color:var(--white);letter-spacing:.5px}
.hero-text{position:absolute;left:0;width:1200px;top:287px;text-align:center;font-family:"Open Sans",sans-serif;font-size:13px;line-height:18px;color:var(--white)}
.btn-light{position:absolute;background:var(--white);color:#333;font-family:"Open Sans",sans-serif;font-size:12px;display:flex;align-items:center;justify-content:center}
.hero-arrow{position:absolute;top:291px;width:27px;height:30px;background:rgba(255,255,255,.25);display:flex;align-items:center;justify-content:center}

/* strip */
.cta-strip{position:absolute;left:0;top:695px;width:1200px;height:57px;background:var(--strip)}
.cta-text{position:absolute;left:210px;top:22px;font-family:"Open Sans",sans-serif;font-weight:700;font-size:11.5px;color:#222;letter-spacing:.4px}
.btn-dark{position:absolute;left:867px;top:12px;width:120px;height:34px;background:var(--black);color:var(--white);font-family:"Open Sans",sans-serif;font-weight:700;font-size:11px;display:flex;align-items:center;justify-content:center}

/* sections */
.section-title{position:absolute;left:0;width:1200px;text-align:center;font-size:28px;font-weight:300;color:var(--ink)}
.title-rule{position:absolute;left:570px;width:60px;height:1px;background:var(--line)}
.photo{position:absolute}
.service-label{position:absolute;width:262px;text-align:center;font-size:11px;letter-spacing:2.5px;color:#444}
.about-title{position:absolute;left:660px;width:328px;top:1396px;text-align:center;font-size:29px;font-weight:300;line-height:36px}
.about-text{position:absolute;left:655px;width:338px;top:1518px;text-align:center;font-family:"Open Sans",sans-serif;font-size:13px;line-height:25px;color:#333}
.btn-outline{position:absolute;border:1px solid #999;background:var(--white);color:#333;font-family:"Open Sans",sans-serif;font-size:12px;display:flex;align-items:center;justify-content:center}
.play{position:absolute;left:346px;top:1493px;width:58px;height:58px;border-radius:50%;background:rgba(255,255,255,.5);display:flex;align-items:center;justify-content:center}
.project-overlay{position:absolute;left:625px;top:1940px;width:174px;height:166px;background:var(--white);text-align:center}
.project-overlay h3{font-family:"Open Sans",sans-serif;font-weight:600;font-size:12px;margin-top:50px;color:#222}
.project-overlay p{font-family:"Open Sans",sans-serif;font-size:10px;line-height:16px;color:#444;margin-top:10px}

/* footer */
.site-footer{position:absolute;left:0;top:2235px;width:1200px;height:452px;background:var(--footer)}
.footer-col{position:absolute;top:90px}
.footer-col h4{font-size:12px;font-weight:400;letter-spacing:2.6px;color:#333}
.footer-col ul{list-style:none;margin-top:33px}
.footer-col li{font-size:10px;color:#555;height:37.6px;letter-spacing:.5px}
.footer-bottom{position:absolute;top:400px;font-size:9.5px;color:#555;letter-spacing:.5px}
.social{position:absolute;top:396px;left:841px;display:flex;gap:33px}
.social span{width:14px;height:14px;border-radius:50%;background:#6a6a6a;display:block}
</style>
</head>
<body>

<header class="site-header">
  <div class="contact-item" style="left:439px">
    <div class="contact-icon">
      <svg width="18" height="13" viewBox="0 0 18 13"><rect x="0" y="0" width="18" height="13" fill="#333"/><path d="M0 0 L9 7 L18 0" stroke="#fff" stroke-width="1.5" fill="none"/></svg>
    </div>
    <div><div class="contact-label">Mail Us @</div><div class="contact-value">hello@norvaledesigns.com</div></div>
  </div>
  <div class="contact-item" style="left:677px">
    <div class="contact-icon">
      <svg width="16" height="16" viewBox="0 0 24 24"><path d="M6.6 10.8a15 15 0 0 0 6.6 6.6l2.2-2.2c.3-.3.7-.4 1-.2 1.1.4 2.3.6 3.6.6.6 0 1 .4 1 1V20c0 .6-.4 1-1 1A17 17 0 0 1 3 4c0-.6.4-1 1-1h3.5c.6 0 1 .4 1 1 0 1.3.2 2.5.6 3.6.1.3 0 .7-.2 1z" fill="none" stroke="#333" stroke-width="1.8"/></svg>
    </div>
    <div><div class="contact-label">Need Help</div><div class="contact-value">555-210-4830</div></div>
  </div>
  <a class="btn-contact">CONTACT US</a>
  <nav class="main-nav">
    <span>HOME</span><span>ABOUT US</span><span>SERVICES</span><span>PROJECT GALLERY</span><span>HOUSE &amp; HOME</span><span>TESTIMONIALS</span>
  </nav>
</header>

<div class="brand">
  <svg class="abs" style="left:0;top:0" width="170" height="134" viewBox="0 0 170 134"><path d="M0 0 H170 V108 Q85 150 0 108 Z" fill="#fff"/><path d="M1 108 Q85 148 169 108" fill="none" stroke="#222" stroke-width="1.5"/></svg>
  <div class="brand-dot"></div>
  <div class="brand-name">Norvale Designs</div>
</div>

<section class="hero" role="img" aria-label="Photo of a brick home with a backyard swimming pool and shrubs">
  <div class="hero-shade"></div>
  <h1 class="hero-title">WE MAKE YOUR DREAM HOME</h1>
  <p class="hero-text">Lorem ipsum dolor sit amet, consectetur adipiscing elit, sed do eiusmod tempor incididunt<br>ut labore et dolore magna aliqua.</p>
  <a class="btn-light" style="left:544px;top:331px;width:112px;height:36px">Learn More</a>
  <span class="hero-arrow" style="left:120px"><svg width="8" height="10"><path d="M7 0 L1 5 L7 10" fill="none" stroke="#fff" stroke-width="1.5"/></svg></span>
  <span class="hero-arrow" style="left:1050px"><svg width="8" height="10"><path d="M1 0 L7 5 L1 10" fill="none" stroke="#fff" stroke-width="1.5"/></svg></span>
</section>

<section class="cta-strip">
  <p class="cta-text">LOREM IPSUM DOLOR SIT AMET CONSECTETUR ADIPISCING ELIT SED DO EIUSMOD TEMPOR INCIDIDUNT.</p>
  <a class="btn-dark">GET START</a>
</section>

<h2 class="section-title" style="top:836px">Our Services</h2>
<div class="title-rule" style="top:887px"></div>
<div class="photo" style="left:161px;top:926px;width:262px;height:251px;background:linear-gradient(160deg,#e6e2dc,#b9a994 55%,#7c8ab0)" role="img" aria-label="Living room with a rustic coffee table and flowers"></div>
<div class="photo" style="left:469px;top:926px;width:262px;height:251px;background:linear-gradient(160deg,#6c6058,#c9c2ba 50%,#8c6a50)" role="img" aria-label="Bathroom with freestanding tub and chandelier"></div>
<div class="photo" style="left:777px;top:926px;width:262px;height:251px;background:linear-gradient(160deg,#e4e4e2,#cfcdca 55%,#8e8170)" role="img" aria-label="White kitchen with wood floors"></div>
<div class="service-label" style="left:161px;top:1206px">FLORAL ARRANGEMENTS</div>
<div class="service-label" style="left:469px;top:1206px">DECORATING</div>
<div class="service-label" style="left:777px;top:1206px">HOLIDAY DECORATING</div>

<div class="photo" style="left:161px;top:1327px;width:428px;height:396px;background:linear-gradient(165deg,#3a3a3a 0%,#d8d8d6 30%,#eeeeec 55%,#555 80%,#2a2a2a)" role="img" aria-label="Kitchen with farmhouse sink and dark granite countertop"></div>
<div class="play"><svg width="18" height="20"><path d="M2 1 L17 10 L2 19 Z" fill="#fff"/></svg></div>
<h2 class="about-title">About<br>Norvale Designs</h2>
<p class="about-text">Lorem ipsum dolor sit amet, consectetur adipiscing elit, sed do eiusmod tempor incididunt ut labore et dolore magna aliqua.</p>
<a class="btn-outline" style="left:763px;top:1617px;width:124px;height:34px">Read More</a>

<h2 class="section-title" style="top:1832px">Our Latest Projects</h2>
<div class="title-rule" style="top:1882px"></div>
<div class="photo" style="left:161px;top:1925px;width:203px;height:197px;background:linear-gradient(160deg,#c9a78a,#e8d8c6 50%,#9d7a5e)" role="img" aria-label="Dining area with round table"></div>
<div class="photo" style="left:387px;top:1925px;width:202px;height:197px;background:linear-gradient(160deg,#6c6058,#c9c2ba 50%,#8c6a50)" role="img" aria-label="Bathroom with freestanding tub"></div>
<div class="photo" style="left:611px;top:1925px;width:202px;height:197px;background:linear-gradient(160deg,#cfcac3,#9c9388)" role="img" aria-label="Finished room project"></div>
<div class="project-overlay">
  <h3>LOREM IPSUM</h3>
  <p>consectetur adipiscing<br>elit, sed do eiusmod.</p>
  <a class="btn-outline" style="left:53px;top:110px;width:68px;height:26px;font-size:10px">Read More</a>
</div>
<div class="photo" style="left:836px;top:1925px;width:203px;height:197px;background:linear-gradient(160deg,#d9cfc3,#b8a493 50%,#8e7866)" role="img" aria-label="Bedroom with upholstered bed and tray ceiling"></div>

<footer class="site-footer">
  <div class="footer-col" style="left:159px"><h4>NAVIGATION</h4><ul><li>Home</li><li>Shop</li><li>Product &amp; Category</li><li>House &amp; Home</li><li>Contact US</li></ul></div>
  <div class="footer-col" style="left:417px"><h4>CATEGORIES</h4><ul><li>Lorem ipsum</li><li>Dolor sit amet</li><li>Consectetur</li><li>Adipiscing</li><li>Iusmod</li></ul></div>
  <div class="footer-col" style="left:659px"><h4>OTHERS</h4><ul><li>My Account</li><li>About Us</li><li>Contact</li><li>Shopping cart</li><li>Checkout</li></ul></div>
  <div class="footer-col" style="left:888px"><h4>CUSTOM SERVICE</h4><ul><li>Shipping &amp; Returns</li><li>Secure Shopping</li><li>International Shipping</li><li>Affiliates</li><li>Contact</li></ul></div>
  <p class="footer-bottom" style="left:159px">© NORVALE DESIGNS 2018. All Rights Reserved.</p>
  <p class="footer-bottom" style="left:421px">TERMS &amp; CONDITIONS &nbsp;&nbsp;|&nbsp;&nbsp; PRIVACY POLICY</p>
  <div class="social"><span></span><span></span><span></span><span></span><span></span></div>
  <svg class="abs" style="left:1116px;top:396px" width="10" height="14" viewBox="0 0 10 14"><path d="M5 13 V2 M1 6 L5 1 L9 6" fill="none" stroke="#555" stroke-width="1.5"/></svg>
</footer>

</body>
</html>
```